Postcard double sided

Title: DWIGHT'S REVENGE

Why would Dwight Kessler align himself with Gordon Pruett?

(photo of two guys)

Dwight approached elected officials that he wanted to run for office, but did not have money to finance his campaign. He wanted other elected officials to finance his campaign. Everyone told him that they would help him get the vote out, but that he needed to finance his own race.

In comes Gordon Pruett.

Gordon Pruett who has a pay to play scheme over at the City, told Dwight he would finance his campaign on one condition.

He needed to run against Steven Hulse.

Why would Dwight want to run with no money?

Backside

DWIGHT'S REVENGE

Dwight decided to run because no one on the school board would terminate Dwight's ex and her new boyfriend who both work for the school district. His ex even filed criminal charges against him that are still pending.

Mug Shot facing left (name the charges Criminal Trespass , and Criminal Mischief (highlight bold letters use two lines) mug shot facing right

Complaint one (then photo with full face) Compliant 2)
(showcharges)

Dwight's ultimate goal is to terminate his ex and her new boyfriend if elected.
Plus Gordon Pruett needs the majority on the school board to do what he does bet.

Kickbacks for Contracts.

They will hire their own contractors!
Say "No" to Dwight's Revenge and Gordon Pruett Money Grab!

Title On Back: all caps: DOMESTIC VIOLENCE

```html
<!DOCTYPE html>
<html lang="en">
<head>
<meta charset="utf-8">
<title>Dwight's Revenge – Postcard</title>
<link rel="stylesheet" href="https://fonts.googleapis.com/css2?family=Rubik+Dirt&family=Montserrat:wght@500;700;800;900&family=Open+Sans:wght@400&family=Oswald:wght@600&display=swap">
<style>
  :root {
    --red: #d10000;
    --blue: #0f4db3;
    --white: #ffffff;
    --stage: #7a7a7a;
    --ink: #222222;
  }
  * { box-sizing: border-box; margin: 0; padding: 0; }
  html, body { width: 851px; height: 1200px; overflow: hidden; }
  body { background: var(--stage); position: relative; font-family: "Open Sans", sans-serif; }

  .card { position: absolute; left: 89px; width: 673px; height: 481px; background: var(--red); overflow: hidden; }
  .card--front { top: 80px; }
  .card--back { top: 635px; }

  .title {
    position: absolute; left: 0; width: 100%; text-align: center; white-space: nowrap;
    font-family: "Rubik Dirt", sans-serif; color: var(--white);
    line-height: 1; letter-spacing: 0.5px;
  }

  /* Front */
  .front-band { position: absolute; left: 0; top: 199px; width: 100%; height: 173px; background: var(--white); }
  .front-title { top: 28px; font-size: 56px; }
  .question {
    position: absolute; left: 41px; top: 107px; width: 309px; height: 54px;
    background: var(--white); border-radius: 4px 4px 0 0;
    display: flex; align-items: center; justify-content: center; text-align: center;
    font-family: "Montserrat", sans-serif; font-weight: 700; font-size: 14px; line-height: 1.4; color: var(--red);
  }
  .story {
    position: absolute; left: 41px; width: 309px; background: var(--blue); color: var(--white);
    text-align: center; font-size: 12.4px; line-height: 1.32;
    display: flex; align-items: center; justify-content: center; padding: 0 10px;
  }
  .story--one { top: 161px; height: 125px; }
  .story--two { top: 317px; height: 78px; border-radius: 0 0 4px 4px; padding-bottom: 6px; }
  .callout {
    position: absolute; left: 41px; top: 286px; width: 309px; height: 31px;
    background: var(--red); border-radius: 3px; color: var(--white);
    display: flex; align-items: center; justify-content: center;
    font-family: "Montserrat", sans-serif; font-weight: 700; font-size: 14px;
  }
  .condition {
    position: absolute; left: 41px; top: 400px; width: 320px; white-space: nowrap;
    font-family: "Montserrat", sans-serif; font-weight: 800; font-size: 14.8px; color: var(--white);
  }
  .photo-pair {
    position: absolute; left: 368px; top: 107px; width: 275px; height: 320px;
    background: linear-gradient(160deg, #2a4a9a 0%, #1c2f6a 55%, #1b1b22 100%);
  }
  .photo-pair::after {
    content: ""; position: absolute; left: 7px; top: 8px; right: 7px; bottom: 8px;
    border: 1px solid var(--white);
  }
  .front-footer {
    position: absolute; left: 0; bottom: 0; width: 100%; height: 54px; background: var(--blue);
    display: flex; align-items: center; justify-content: center; white-space: nowrap;
    font-family: "Montserrat", sans-serif; font-weight: 800; font-size: 21px; color: var(--white); letter-spacing: 0.3px;
  }

  /* Back */
  .back-lower { position: absolute; left: 0; top: 202px; width: 100%; height: 279px; background: var(--blue); }
  .back-title { top: 29px; font-size: 52px; }
  .motive {
    position: absolute; left: 34px; top: 100px; width: 282px;
    font-size: 12.4px; line-height: 1.33; color: var(--white);
  }
  .goals { position: absolute; left: 34px; top: 216px; width: 282px; list-style: none; }
  .goals::before { content: ""; position: absolute; left: 6.5px; top: 14px; height: 72px; border-left: 1px solid var(--white); }
  .goal {
    position: relative; padding-left: 22px; margin-bottom: 8px;
    font-family: "Montserrat", sans-serif; font-weight: 500; font-size: 12.4px; line-height: 1.27; color: var(--white);
  }
  .goal svg { position: absolute; left: 0; top: 1px; width: 14px; height: 14px; background: var(--blue); }
  .kickbacks {
    position: absolute; left: 34px; top: 315px; width: 276px; height: 33px; background: var(--white);
    display: flex; align-items: center; justify-content: center; white-space: nowrap;
    font-family: "Oswald", sans-serif; font-weight: 600; font-size: 21px; color: var(--red); letter-spacing: 0.2px;
  }
  .contractors {
    position: absolute; left: 30px; top: 354px; width: 288px; text-align: center; white-space: nowrap;
    font-family: "Oswald", sans-serif; font-weight: 600; font-size: 17.5px; color: var(--white);
  }
  .say-no { position: absolute; left: 34px; top: 385px; height: 48px; display: flex; align-items: center; white-space: nowrap; }
  .say-no__say { font-family: "Montserrat", sans-serif; font-weight: 900; font-size: 34px; color: var(--white); margin-right: 7px; }
  .say-no__no {
    width: 96px; height: 48px; background: var(--red); color: var(--white);
    display: flex; align-items: center; justify-content: center;
    font-family: "Montserrat", sans-serif; font-weight: 900; font-size: 34px;
  }
  .say-no__to {
    margin-left: 7px; font-family: "Montserrat", sans-serif; font-weight: 800; font-size: 12.5px; line-height: 1.1; color: var(--white);
  }
  .money-grab {
    position: absolute; left: 34px; top: 442px; width: 286px; white-space: nowrap;
    font-family: "Montserrat", sans-serif; font-weight: 800; font-size: 14.8px; color: var(--white);
  }
  .evidence { position: absolute; left: 326px; top: 100px; width: 322px; height: 357px; background: var(--white); }
  .mugshot {
    position: absolute; top: 5px; width: 152px; height: 175px;
    background: linear-gradient(180deg, #8d8d8f 0%, #7a7a7c 65%, #2f4a38 100%);
  }
  .mugshot--left { left: 7px; }
  .mugshot--right { left: 164px; }
  .charge {
    position: absolute; top: 180px; width: 152px; height: 33px; background: var(--red); border-radius: 0 0 4px 4px;
    display: flex; align-items: center; justify-content: center; white-space: nowrap;
    font-family: "Oswald", sans-serif; font-weight: 600; font-size: 17.5px; color: var(--white);
  }
  .charge--left { left: 7px; }
  .charge--right { left: 164px; }
  .complaint {
    position: absolute; top: 229px; width: 92px; height: 112px; padding: 4px 3px;
    font-size: 3.6px; line-height: 1.4; color: var(--ink);
  }
  .complaint--one { left: 13px; }
  .complaint--two { left: 219px; }
  .complaint p { margin-bottom: 3px; }
  .complaint__sign { border-top: 0.6px solid var(--ink); width: 45px; margin: 12px 0 0 40px; }
  .portrait {
    position: absolute; left: 113px; top: 226px; width: 95px; height: 120px;
    background: linear-gradient(180deg, #7c7c80 0%, #6a6a6e 60%, #223a2c 100%);
  }
</style>
</head>
<body>

<section class="card card--front">
  <div class="front-band"></div>
  <h1 class="title front-title">DWIGHT'S REVENGE</h1>
  <h2 class="question">Why would Dwight Kessler<br>align himself with Gordon Pruett?</h2>
  <p class="story story--one">Dwight approached elected officials that he wanted to run for office, but did not have money to finance his campaign. He wanted other elected officials to finance his campaign. Everyone told him that they would help him get the vote out, but that he needed to finance his own race.</p>
  <p class="callout">In comes Gordon Pruett.</p>
  <p class="story story--two">Gordon Pruett who has a pay to play scheme over at the City, told Dwight he would finance his campaign on one condition.</p>
  <p class="condition">He needed to run against Steven Hulse.</p>
  <div class="photo-pair" role="img" aria-label="Photo of Dwight Kessler and Gordon Pruett standing together in suits at a campaign event"></div>
  <p class="front-footer">WHY WOULD DWIGHT WANT TO RUN WITH NO MONEY?</p>
</section>

<section class="card card--back">
  <div class="back-lower"></div>
  <h1 class="title back-title">DOMESTIC VIOLENCE</h1>
  <p class="motive">Dwight decided to run because no one on the school board would terminate Dwight's ex and her new boyfriend who both work for the school district. His ex even filed criminal charges against him that are still pending.</p>

  <ul class="goals">
    <li class="goal">
      <svg viewBox="0 0 14 14"><circle cx="7" cy="7" r="6.2" fill="none" stroke="#fff" stroke-width="1"/><path d="M4 7.2l2 2 4-4" fill="none" stroke="#fff" stroke-width="1.1"/></svg>
      Dwight's ultimate goal is to terminate his ex and her new boyfriend if elected.
    </li>
    <li class="goal">
      <svg viewBox="0 0 14 14"><circle cx="7" cy="7" r="6.2" fill="none" stroke="#fff" stroke-width="1"/><path d="M4 7.2l2 2 4-4" fill="none" stroke="#fff" stroke-width="1.1"/></svg>
      Plus Gordon Pruett needs the majority on the school board to do what he does bet.
    </li>
  </ul>

  <p class="kickbacks">KICKBACKS FOR CONTRACTS.</p>
  <p class="contractors">They will hire their own contractors!</p>
  <div class="say-no">
    <span class="say-no__say">SAY</span>
    <span class="say-no__no">NO</span>
    <span class="say-no__to">TO DWIGHT'S<br>REVENGE</span>
  </div>
  <p class="money-grab">and Gordon Pruett Money Grab!</p>

  <div class="evidence">
    <div class="mugshot mugshot--left" role="img" aria-label="Booking photo, profile facing left"></div>
    <p class="charge charge--left">Criminal Trespass</p>
    <div class="mugshot mugshot--right" role="img" aria-label="Booking photo, profile facing right"></div>
    <p class="charge charge--right">Criminal Mischief</p>

    <div class="complaint complaint--one">
      <p>THE STATE OF TEXAS<br>COUNTY OF MARLOW<br>COMPLAINT</p>
      <p>Affiant swears the accused entered the property without consent.</p>
      <p>Sworn and subscribed before me.</p>
      <div class="complaint__sign"></div>
    </div>
    <div class="portrait" role="img" aria-label="Booking photo, facing front"></div>
    <div class="complaint complaint--two">
      <p>THE STATE OF TEXAS<br>COUNTY OF MARLOW<br>COMPLAINT</p>
      <p>Affiant swears the accused damaged the property without consent.</p>
      <p>Sworn and subscribed before me.</p>
      <div class="complaint__sign"></div>
    </div>
  </div>
</section>

</body>
</html>
```